Design some Business Cards

I need a business card designed, in English on one side, and in Russian on the other side, which will incorporate my client’s logo (logo in different formats is in zip folder attached). The name, details/info required on the business card are in the document in the zip folder.

Please let me know if you have any questions. I will provide feedback on the entries as quickly as I can.

Regards.

```html
<!DOCTYPE html>
<html lang="en">
<head>
<meta charset="utf-8">
<title>Costa Vesta — Business Cards</title>
<link rel="stylesheet" href="https://fonts.googleapis.com/css2?family=Arimo:wght@400;700&display=swap">
<style>
  :root {
    --backdrop: #e9e7e3;
    --card-white: #ffffff;
    --ink: #2b2b2b;
    --brand: #2f6fb8;
    --charcoal-light: #444444;
    --charcoal-dark: #1c1c1c;
    --accent-yellow: #eed94a;
    --text-light: #f2f2f2;
    --blue-light: #3a86d4;
    --blue-dark: #173f95;
    --rule-light: rgba(255,255,255,0.35);
  }
  * { margin: 0; padding: 0; box-sizing: border-box; }
  html, body {
    width: 1200px; height: 912px; overflow: hidden;
    background: var(--backdrop);
    font-family: "Arimo", Arial, sans-serif;
  }
  .sheet { position: relative; width: 1200px; height: 912px; }
  .card {
    position: absolute; left: 280px; width: 640px; height: 366px;
    background: var(--card-white); overflow: hidden;
    box-shadow: 0 6px 22px rgba(0,0,0,0.18);
  }
  .card--dark { top: 60px; }
  .card--blue { top: 486px; }
  .card__bg { position: absolute; inset: 0; width: 100%; height: 100%; }

  .brand { position: absolute; }
  .brand__name {
    font-weight: 400; font-size: 34px; letter-spacing: 2px;
    color: var(--brand); text-transform: uppercase; white-space: nowrap;
  }
  .brand__url {
    margin-top: 6px; font-size: 12px; font-weight: 700;
    letter-spacing: 3.2px; color: var(--ink); white-space: nowrap;
  }
  .card--dark .brand { left: 30px; top: 158px; }
  .card--dark .brand__name { font-size: 26px; letter-spacing: 1.5px; }
  .card--dark .brand__url { font-size: 10px; letter-spacing: 2.6px; margin-top: 5px; }
  .card--blue .brand { left: 44px; top: 50px; }

  .contact { position: absolute; color: var(--text-light); font-size: 13px; line-height: 1.5; white-space: nowrap; }
  .contact__name { font-size: 21px; margin-bottom: 6px; }
  .contact__role { font-size: 14px; margin-bottom: 10px; }

  .card--dark .contact__name { color: var(--accent-yellow); }
  .card--dark .contact--en { left: 340px; top: 44px; }
  .card--dark .contact--ru { left: 340px; top: 200px; }
  .card--dark .divider {
    position: absolute; left: 340px; top: 180px; width: 270px; height: 1px;
    background: var(--rule-light);
  }

  .card--blue .contact__name { font-size: 17px; font-weight: 700; color: #fff; }
  .card--blue .contact__role { margin-bottom: 14px; }
  .card--blue .contact--en { left: 44px; top: 214px; }
  .card--blue .contact--ru { left: 352px; top: 170px; }
  .card--blue .contact--ru .contact__name { font-weight: 400; }
  .card--blue .contact--en .contact__name { text-transform: uppercase; }
  .card--blue .divider {
    position: absolute; left: 322px; top: 168px; width: 1px; height: 170px;
    background: var(--rule-light);
  }
</style>
</head>
<body>
<main class="sheet">

  <section class="card card--dark" aria-label="Business card, charcoal edition">
    <svg class="card__bg" viewBox="0 0 640 366" preserveAspectRatio="none" aria-hidden="true">
      <defs>
        <linearGradient id="charcoal" x1="0" y1="0" x2="1" y2="1">
          <stop offset="0" stop-color="#444444"/>
          <stop offset="1" stop-color="#1c1c1c"/>
        </linearGradient>
      </defs>
      <path d="M312 0 Q272 183 322 366 L640 366 L640 0 Z" fill="url(#charcoal)"/>
    </svg>

    <div class="brand">
      <div class="brand__name">Costa Vesta</div>
      <div class="brand__url">www.costavesta.com.ua</div>
    </div>

    <div class="contact contact--en">
      <div class="contact__name">Oliver Hartwell</div>
      <div class="contact__role">Director</div>
      <div>oliver@costavesta.com.ua</div>
      <div>+34 600 214 357</div>
    </div>
    <div class="divider"></div>
    <div class="contact contact--ru" lang="ru">
      <div class="contact__name">Оливер Хартвелл</div>
      <div class="contact__role">Директор</div>
      <div>oliver@costavesta.com.ua</div>
      <div>+38 050 482 19 63</div>
      <div>+34 60 021 43 57</div>
    </div>
  </section>

  <section class="card card--blue" aria-label="Business card, blue edition">
    <svg class="card__bg" viewBox="0 0 640 366" preserveAspectRatio="none" aria-hidden="true">
      <defs>
        <linearGradient id="ocean" x1="0" y1="1" x2="1" y2="0">
          <stop offset="0" stop-color="#173f95"/>
          <stop offset="1" stop-color="#3a86d4"/>
        </linearGradient>
      </defs>
      <path d="M0 196 Q320 176 640 120 L640 366 L0 366 Z" fill="url(#ocean)"/>
    </svg>

    <div class="brand">
      <div class="brand__name">Costa Vesta</div>
      <div class="brand__url">www.costavesta.com.ua</div>
    </div>

    <div class="contact contact--en">
      <div class="contact__name">Marina Solovey</div>
      <div class="contact__role">Director</div>
      <div>marina@costavesta.com.ua</div>
      <div>+34 611 538 204</div>
    </div>
    <div class="divider"></div>
    <div class="contact contact--ru" lang="ru">
      <div class="contact__name">Марина Соловей</div>
      <div class="contact__role">Директор</div>
      <div>marina@costavesta.com.ua</div>
      <div>+38 050 482 19 63</div>
      <div>+34 61 153 82 04</div>
    </div>
  </section>

</main>
</body>
</html>
```